Lanternfold Advisory Business Cards

We need a new layout for our business cards. We have a logo already. But we might be interested in only using the Lanternfold portion of the logo. It has been uploaded.

We would like cards that are not overly busy. Clean. Modern. Perhaps a gray color for one side.

On the back, we would like to have the lanternfold part of the logo and "Take the Leap, we've got you!"

Our business provides medics and safety training for corporate clients. Our website is www.lanternfoldadvisoryllc.example.

Industry/Entity Type

Business

Contact Information for Business Card

We want include name, email address, cell phone, main line number, and website URL on the front. Use the following as an example: Dana Kovrin, dana@lanternfoldadvisoryllc.example, 804.321.7788 (cell), 804.432.919, and www.lanternfoldadvisoryllc.example.

Font styles to use
Serif
Sans Serif

Requirements
Must have
• All required information. Back side logo with "Take the leap, we will catch you!"
Nice to have
• If possible, we would like to consider creating a card in a non-standard shape. Perhaps, the shape of a lanternfold. Just interested in understanding the option.

```html
<!DOCTYPE html>
<html lang="en">
<head>
<meta charset="utf-8">
<title>Lanternfold Advisory – Business Card</title>
<link rel="stylesheet" href="https://fonts.googleapis.com/css2?family=Crimson+Pro:wght@600&family=Source+Sans+3:wght@400;500&display=swap">
<style>
  :root {
    --canvas-bg: #d9d6d1;
    --card-top: #f4f3f1;
    --card-bottom: #e6e5e3;
    --card-edge: #c9c8c6;
    --brand-blue: #253f7a;
    --name-blue: #2d4a80;
    --text-grey: #3f3f42;
    --art-light: #dfe5ef;
    --art-mid: #c3cde0;
  }
  * { margin: 0; padding: 0; box-sizing: border-box; }
  html, body {
    width: 1200px;
    height: 970px;
    overflow: hidden;
    background: var(--canvas-bg);
  }
  .business-card {
    position: absolute;
    left: 100px;
    top: 207px;
    width: 1000px;
    height: 556px;
    background: linear-gradient(160deg, var(--card-top), var(--card-bottom));
    border: 1px solid var(--card-edge);
    box-shadow: 0 10px 30px rgba(0,0,0,0.12);
  }
  .company-name {
    position: absolute;
    left: 73px;
    top: 84px;
    font-family: "Crimson Pro", serif;
    font-weight: 600;
    font-size: 44px;
    line-height: 50px;
    font-variant: small-caps;
    letter-spacing: 1px;
    color: var(--brand-blue);
  }
  .contact-block {
    position: absolute;
    left: 73px;
    top: 340px;
    font-family: "Source Sans 3", sans-serif;
    color: var(--text-grey);
  }
  .person-name {
    font-size: 27px;
    font-weight: 500;
    color: var(--name-blue);
    text-transform: uppercase;
    letter-spacing: 0.3px;
    margin-bottom: 14px;
  }
  .contact-line {
    font-size: 20.5px;
    line-height: 28px;
    font-weight: 400;
  }
  .brand-art {
    position: absolute;
    left: 611px;
    top: 89px;
    width: 317px;
    height: 374px;
  }
</style>
</head>
<body>
  <div class="business-card">
    <h1 class="company-name">Lanternfold<br>Advisory</h1>

    <div class="contact-block">
      <p class="person-name">Dana Kovrin</p>
      <p class="contact-line">M: 804.321.7788 · T: 804.432.919</p>
      <p class="contact-line">E: dana@lanternfoldadvisoryllc.example</p>
      <p class="contact-line">www.lanternfoldadvisoryllc.example</p>
    </div>

    <svg class="brand-art" viewBox="0 0 317 374" role="img" aria-label="Brand illustration area: navy silhouette artwork">
      <defs>
        <radialGradient id="artFill" cx="50%" cy="45%" r="60%">
          <stop offset="0%" stop-color="var(--art-mid)"/>
          <stop offset="100%" stop-color="var(--art-light)" stop-opacity="0"/>
        </radialGradient>
      </defs>
      <rect width="317" height="374" fill="url(#artFill)"/>
    </svg>
  </div>
</body>
</html>
```